Infographic for Ed Non-Profit Showing Parts of a School Design

We need an infographic done that depicts the parts of a school design (or what we call a blueprint). It will be used to help schools understand the different things they need to design and develop to have a coherent school design. These parts include:

Local Context - The larger context in which the learning environment exists.

Purpose - The overarching role the learning environment must play.

Graduate Aims -The learning outcomes the environment will drive toward.

Design Principles - Core characteristics of the learning environment and the experiences learners have within it that weave across the design and help it feel coherent.

Student Experiences - Programmed activities that key stakeholders—such as learners, educators, and families—engage in within the learning environment.

System Elements - The various approaches, structures, and resources related to areas like curriculum, hiring, technology, and more that enable experiences..

Attachments
Internally Created Blueprint Visuals - We have various working drafts that we've done internally but we want to elevate the design now. I've attached these in one document. They show connections between the parts well but are not attractive. The final visual does not need to look like any of these, I am including it just to give an idea of what we've tried. I have a feeling there are lots of other solutions we have not explored yet.

Style Guide - I attached a few pages from our style guide. We do not really have an illustrations or graphic style.

Guide to School Design Blueprint - This is an early draft of one place the infographic will be used. We'd want to put it in the introduction and pieces of it in each of the corresponding sections.

Target Market(s)

School and school system (fdistrict) leaders

Font styles to use
Serif
Other font styles liked:
• Open sans, Bebas Nue, Roberts (see style guide)

Requirements
Must have
• The most critical things are:
1- Include all the parts of a school design (see above).

2- Show how they relate to each other (e.g. system elements enable experiences, experiences drive toward aims, grad aims drive toward purpose, design principles cut across all parts of school design and bring coherence, local context surround the whole school design)
Nice to have
• Pieces of the larger design could be broken or pulled apart and used flexibly. For example, if we want to use the graphic in a deck of slides for an event or in a document we could show the whole graphic or just parts of it.
Should not have
• imagery that is overly stereotypical regarding schools. No old fashioned school houses, no students sitting in row, etc.

```html
<!DOCTYPE html>
<html lang="en">
<head>
<meta charset="utf-8">
<title>School Design Blueprint</title>
<link href="https://fonts.googleapis.com/css2?family=Open+Sans:wght@300;400;700&display=swap" rel="stylesheet">
<style>
  :root {
    --stage: #16264a;
    --paper: #ffffff;
    --teal: #50827b;
    --red: #cf4a4c;
    --navy: #334b7c;
    --grey: #c4c5c9;
    --orange: #e8a640;
    --plum: #a1287e;
    --ink: #3f3f44;
    --white: #ffffff;
    --shadow: 4px 6px 10px rgba(0,0,0,0.35);
  }
  * { box-sizing: border-box; margin: 0; padding: 0; }
  html, body {
    width: 1200px; height: 1200px; overflow: hidden;
    background: var(--stage);
    font-family: "Open Sans", Arial, sans-serif;
  }
  .sheet {
    position: absolute; left: 138px; top: 0;
    width: 923px; height: 1200px;
    background: var(--paper); overflow: hidden;
  }
  .sheet-backdrop { position: absolute; inset: 0; }
  .brand {
    position: absolute; left: 118px; top: 68px;
    display: flex; align-items: center; gap: 12px;
  }
  .brand-square { width: 34px; height: 34px; background: var(--red); }
  .brand-name {
    font-size: 44px; font-weight: 400; color: var(--red); letter-spacing: 0.5px;
  }
  .tier {
    position: absolute; left: 118px; width: 672px;
    color: var(--white); text-align: center; box-shadow: var(--shadow);
  }
  .tier-title { font-weight: 700; font-size: 22px; letter-spacing: 0.3px; }
  .tier-text { font-weight: 300; font-size: 18.5px; line-height: 1.12; }
  .tier--purpose { top: 180px; height: 119px; background: var(--red); padding-top: 18px; }
  .tier--purpose .tier-title { font-size: 45px; line-height: 1.1; margin-bottom: 4px; }
  .tier--aims { top: 334px; height: 85px; background: var(--navy); padding-top: 18px; }
  .tier--local { top: 1065px; height: 83px; left: 119px; background: var(--plum); padding-top: 16px; }
  .pointer { position: absolute; left: 50%; top: -14px; margin-left: -8px; }
  .coherence-frame {
    position: absolute; left: 101px; top: 444px; width: 707px; height: 604px;
    background: var(--grey); box-shadow: var(--shadow);
  }
  .tier--experiences { top: 459px; height: 173px; background: var(--teal); padding-top: 22px; }
  .tier--experiences .tier-text { margin-top: 4px; }
  .experience-split {
    position: absolute; left: 31px; right: 21px; top: 113px; bottom: 10px;
    border-top: 1px solid rgba(255,255,255,0.85);
    display: grid; grid-template-columns: 192px 240px 1fr;
  }
  .experience-split span {
    font-size: 13px; font-weight: 300; padding-top: 18px;
  }
  .experience-split span + span { border-left: 1px solid rgba(255,255,255,0.85); }
  .principles {
    position: absolute; left: 101px; width: 707px; top: 652px;
    text-align: center; color: var(--ink);
  }
  .principles .tier-title { color: #444448; }
  .principles .tier-text { margin-top: 4px; font-size: 18.5px; line-height: 1.2; }
  .tier--systems { top: 757px; height: 272px; left: 119px; background: var(--orange); padding-top: 18px; }
  .tier--systems .tier-text { margin-top: 4px; line-height: 1.2; }
  .system-grid {
    margin: 22px 12px 0 8px;
    display: grid; grid-template-columns: repeat(5, 1fr); row-gap: 22px;
  }
  .system-grid span { font-size: 13px; font-weight: 300; line-height: 1.2; }
</style>
</head>
<body>
  <main class="sheet">
    <svg class="sheet-backdrop" width="923" height="1200" viewBox="0 0 923 1200" aria-hidden="true">
      <polygon points="0,293 923,123 923,1200 0,1200" fill="#50827b"/>
      <polygon points="0,1038 923,1160 923,1200 0,1200" fill="#e8a640"/>
    </svg>

    <div class="brand">
      <span class="brand-square"></span>
      <span class="brand-name">Quorvane</span>
    </div>

    <section class="tier tier--purpose">
      <h1 class="tier-title">PURPOSE</h1>
      <p class="tier-text">The overarching role the learning environment must play.</p>
    </section>

    <section class="tier tier--aims">
      <svg class="pointer" width="16" height="14" viewBox="0 0 16 14" aria-hidden="true"><polygon points="8,0 16,14 0,14" fill="#334b7c"/></svg>
      <h2 class="tier-title">GRADUATE AIMS</h2>
      <p class="tier-text">The learning outcomes the environment will drive toward.</p>
    </section>

    <div class="coherence-frame"></div>

    <section class="tier tier--experiences">
      <svg class="pointer" width="16" height="14" viewBox="0 0 16 14" aria-hidden="true"><polygon points="8,0 16,14 0,14" fill="#50827b"/></svg>
      <h2 class="tier-title">STUDENT EXPERIENCES</h2>
      <p class="tier-text">Programmed activities that key stakeholders—such as learners,<br>educators, and families—engage in within the learning environment.</p>
      <div class="experience-split">
        <span>Students Experiences</span>
        <span>Family Experiences</span>
        <span>Staff Experiences</span>
      </div>
    </section>

    <section class="principles">
      <h2 class="tier-title">DESIGN PRINCIPLES</h2>
      <p class="tier-text">Core characteristics of the learning environment and the experiences<br>learners have within it that weave across the design and help it feel coherent.</p>
    </section>

    <section class="tier tier--systems">
      <h2 class="tier-title">SYSTEM ELEMENTS</h2>
      <p class="tier-text">The various approaches, structures, and resources related to areas<br>like curriculum, hiring, technology, and more that enable experiences..</p>
      <div class="system-grid">
        <span>Community &amp;<br>Family<br>Partnerships</span>
        <span>Continuous<br>Learning &amp;<br>Improvement</span>
        <span>Technology &amp; Tech<br>Infrastructure</span>
        <span>Scheduling &amp;<br>Use of Time</span>
        <span>Curriculum,<br>Instruction &amp;<br>Assessment</span>
        <span>School<br>Community &amp;<br>Culture</span>
        <span>Adult Roles,<br>Hiring &amp;<br>Development</span>
        <span>Space &amp;<br>Facilities</span>
        <span>Budget &amp;<br>Operations</span>
        <span>Communications</span>
      </div>
    </section>

    <section class="tier tier--local">
      <h2 class="tier-title">LOCAL CONTEXT</h2>
      <p class="tier-text">The larger context in which the learning environment exists.</p>
    </section>
  </main>
</body>
</html>
```